Looking to overhaul my current Wordpress website

Current have a website www.qoradatrix.com in wordpress, lack the skills or design flare to make it look and work better and more corporate professional.
We are a technology solution provider and software developer.
Updates
I think i have successfully uploaded my logo to assist with the wordpress theme and framework samples you will be providing.
Post me a message if you can locate it.
Target Market(s)
Small to business
Industry/Entity Type
Software
Font styles to use
Sans Serif
Requirements
Must have
- Must work on any device anywhere anytime, mobile ready in addition to traditional browser. Must be in work press for ongoing maintenance.
Nice to have
- use these website for a look and feel http://www.fernwaleclear.com.au/ http://www.tarvolinadvisory.com/work http://www.tarvolinadvisory.com/method
http://www.plumcrestlab.com/
Should not have
- No Flash!!,

```html
<!DOCTYPE html>
<html lang="en">
<head>
<meta charset="utf-8">
<title>Qora Datrix</title>
<link href="https://fonts.googleapis.com/css2?family=Open+Sans:wght@400;600;700&family=Oswald:wght@500;600&family=Archivo+Black&display=swap" rel="stylesheet">
<style>
:root{
  --blue:#0b8fd0;
  --blue-dark:#0a6fa8;
  --navy:#1d4f91;
  --ink:#333;
  --muted:#555;
  --nav-active:#222;
  --white:#fff;
  --line:#8fc7e8;
}
*{margin:0;padding:0;box-sizing:border-box}
html,body{width:812px;height:1200px;overflow:hidden;background:var(--white)}
body{position:relative;font-family:"Open Sans",Arial,sans-serif;color:var(--ink)}
.abs{position:absolute}
.topline{left:0;top:0;width:812px;height:2px;background:var(--blue)}
.account{left:617px;top:0;width:101px;height:18px;background:var(--blue);color:var(--white);font-size:8px;display:flex;align-items:center;justify-content:space-around;border-radius:0 0 2px 2px}
.account i{width:1px;height:9px;background:rgba(255,255,255,.6)}
.brand{left:94px;top:14px;font-family:"Oswald",sans-serif;font-weight:600;font-size:19px;color:var(--blue)}
.tagline{left:94px;top:43px;font-size:8.2px;color:var(--muted)}
.nav{left:0;top:72px;width:812px;height:25px;background:var(--blue)}
.nav ul{position:absolute;left:94px;top:0;display:flex;list-style:none;height:25px}
.nav li{color:var(--white);font-size:10.2px;font-weight:600;padding:0 14px;line-height:25px;border-right:1px solid rgba(255,255,255,.25)}
.nav li.active{background:var(--nav-active);padding:0 16px}
.search{left:694px;top:72px;width:24px;height:25px;background:var(--nav-active)}
.hero{left:0;top:97px;width:812px;height:313px;background:radial-gradient(ellipse at 70% 30%,#b6a7dc 0%,#8a78c8 30%,#5a46b0 65%,#3a2a8e 100%)}
.hero h1{position:absolute;left:94px;top:60px;font-family:"Archivo Black",sans-serif;font-weight:400;font-size:24.5px;line-height:25px;color:var(--white)}
.hero p{position:absolute;left:94px;top:148px;width:250px;font-size:9.4px;line-height:12.4px;color:var(--white);text-align:justify}
.devices{left:388px;top:140px;width:332px;height:215px;background:linear-gradient(160deg,#e9e9ee,#9fa0b4 60%,#5f5a86);border-radius:6px;opacity:.9}
.sec-title{font-family:"Oswald",sans-serif;font-weight:500;font-size:12px;color:var(--blue-dark)}
.welcome-title{left:94px;top:424px}
.welcome-rule{left:252px;top:437px;width:250px;height:1px;background:var(--blue)}
.welcome-text{left:94px;top:451px;width:411px;font-size:8.1px;line-height:12.45px;color:var(--muted);text-align:justify}
.news-title{left:543px;top:424px}
.news-rule{left:573px;top:437px;width:119px;height:1px;background:var(--blue)}
.arrows{left:692px;top:425px;display:flex;gap:1px}
.arrows span{width:12px;height:12px;background:#666;display:block}
.arrows span.on{background:var(--blue)}
.news-item{left:543px;width:180px;height:56px;border-bottom:1px dotted var(--line)}
.news-thumb{position:absolute;left:1px;top:2px;width:36px;height:34px;background:linear-gradient(135deg,#c9ced6,#6a7282);border:1px solid #ccc}
.news-body{position:absolute;left:44px;top:0;width:136px;font-size:7.3px;line-height:9.5px;color:var(--ink)}
.news-body b{display:block}
.news-body em{color:var(--navy)}
.service-title{left:94px;top:636px}
.card{width:200px}
.card .photo{width:200px;height:131px;border:3px solid #e6e6e6;box-shadow:0 3px 4px rgba(0,0,0,.2)}
.card h3{font-weight:400;font-size:10.3px;margin-top:7px;color:#222}
.card p{font-size:8.1px;line-height:12.4px;color:var(--muted);margin-top:3px}
.footer{left:0;top:1066px;width:812px;height:134px;background:var(--blue);color:var(--white)}
.footer h4{position:absolute;top:10px;font-weight:400;font-size:11.5px}
.footer ul{position:absolute;list-style:none;font-size:8px;line-height:12.45px}
.menu li{color:#e3f2fb}
.menu li.active{color:#111}
.social li{display:flex;align-items:center;gap:7px;height:21.5px}
.social li span{width:15px;height:15px;background:var(--blue-dark);border:1px solid rgba(255,255,255,.3)}
.contact{font-size:8px;line-height:12.4px}
.map{left:584px;top:34px;width:134px;height:81px;background:linear-gradient(135deg,#ece8df,#d8d4cb);border:1px solid #cfe6f3}
</style>
</head>
<body>
<div class="abs topline"></div>
<div class="abs account"><span>Register</span><i></i><span>Log in</span></div>
<div class="abs brand">Qora Datrix</div>
<div class="abs tagline">We are a diverse group of experienced designers, strategists and technologists ready to make things happen.</div>

<nav class="abs nav">
  <ul>
    <li class="active">Home</li><li>Our Team</li><li>Our Values</li><li>Working With us</li><li>Our service</li><li>Our Solutions</li><li style="border:none">Get in touch</li>
  </ul>
</nav>
<div class="abs search">
  <svg width="24" height="25" viewBox="0 0 24 25"><circle cx="11" cy="11.5" r="4.2" fill="none" stroke="#fff" stroke-width="1.8"/><line x1="14" y1="14.5" x2="17" y2="17.5" stroke="#fff" stroke-width="2"/></svg>
</div>

<section class="abs hero">
  <h1>We love to build<br>Beautiful Applications<br>And Solutions.</h1>
  <p>Beautiful products look great and work in a simple, intuitive manner and the user wants to use the product all the time.<br>A software product’s design language is established upfront, but the details of the experience and interaction layer emerge iteratively as a product is built.</p>
</section>
<div class="abs devices" role="img" aria-label="Website shown on a desktop monitor, tablet and phone"></div>

<h2 class="abs sec-title welcome-title">WelCome to Qora Datrix</h2>
<div class="abs welcome-rule"></div>
<svg class="abs" style="left:493px;top:427px" width="12" height="12" viewBox="0 0 12 12"><g fill="none" stroke="#0b8fd0" stroke-width="1.4"><rect x="1" y="5" width="6" height="3.5" rx="1.7" transform="rotate(-45 4 6.7)"/><rect x="5" y="3" width="6" height="3.5" rx="1.7" transform="rotate(-45 8 4.7)"/></g></svg>
<div class="abs welcome-text">
Qora Datrix was founded in 2007 with the mission to become the go-to teogy consultancy for building world-class, one of a kind, web applications and web based businesses.<br>
We have seen many great ideas killed because of poor execution by technology tehat didn’t treat their work as craft.<br>
We knew we could provide the perfect place for entrepreneurs to come for foueval design and engineering leadership, and where large companies could inject entrepreneurial innovation inir existing product development efforts.<br>
Our team of engineers, product management, user experience and design talent idream-team of talent we will use on our own products, such as Brightnote CRM, and also the same team ours have access to.<br>
By having the best people we’re able to do a few things: attract more great peoitain our great people, build applications faster by being smarter and be able to have the right team in place ten we build applications for ourselves.<br>
In a company like Qora Datrix, engineering and creativity drives the busineur people are all a aligned to
</div>

<h2 class="abs sec-title news-title">NEWS</h2>
<div class="abs news-rule"></div>
<div class="abs arrows">
  <span><svg width="12" height="12"><path d="M7 3 4 6l3 3" fill="none" stroke="#fff" stroke-width="1.3"/></svg></span>
  <span class="on"><svg width="12" height="12"><path d="M5 3l3 3-3 3" fill="none" stroke="#fff" stroke-width="1.3"/></svg></span>
</div>
<div class="abs news-item" style="top:452px">
  <div class="news-thumb" role="img" aria-label="Portrait photo of a businessman"></div>
  <div class="news-body"><b>Hello world!</b>We don’t do ad-hoc, throw-away development.<br><em>Posted by September 4, 2012</em></div>
</div>
<div class="abs news-item" style="top:513px">
  <div class="news-thumb" role="img" aria-label="Photo of business colleagues shaking hands"></div>
  <div class="news-body"><b>Hello world!</b>Long before Qora Datrix was even an sparkle in the eye of the<br><em>Posted by &nbsp;September 5, 2012</em></div>
</div>
<div class="abs news-item" style="top:574px;border:none">
  <div class="news-thumb" role="img" aria-label="Portrait photo of a businessman"></div>
  <div class="news-body"><b>Hello world!</b>This is because of the security fatures in Nimbus OS 2008.<br><em>Posted by September 10, 2012</em></div>
</div>

<h2 class="abs sec-title service-title">Our Service</h2>

<div class="abs card" style="left:94px;top:655px">
  <div class="photo" role="img" aria-label="Team working together at a laptop, tinted blue" style="background:#1a9ad8;display:flex;align-items:center;justify-content:center">
    <svg width="24" height="24" viewBox="0 0 12 12"><g fill="none" stroke="#fff" stroke-width="1.2"><rect x="1" y="5" width="6" height="3.5" rx="1.7" transform="rotate(-45 4 6.7)"/><rect x="5" y="3" width="6" height="3.5" rx="1.7" transform="rotate(-45 8 4.7)"/></g></svg>
  </div>
  <h3>Technology Strategy</h3>
  <p>Lorem ipsum dolor sit amet, consectetur adipiscing elit. Donec nec dignissim lorem. Vestibulum odio ante,malesuada ac auctor vitae, mollis tempus dolor.</p>
</div>
<div class="abs card" style="left:306px;top:655px">
  <div class="photo" role="img" aria-label="Server racks with a hand holding a glowing cloud" style="background:linear-gradient(120deg,#0c2d4a,#1f6d93 55%,#0b1e33)"></div>
  <h3>Wireless Infrastructure Services</h3>
  <p>Lorem ipsum dolor sit amet, consectetur adipiscing elit. Donec nec dignissim lorem. Vestibulum odio ante,malesuada ac auctor vitae, mollis tempus dolor.</p>
</div>
<div class="abs card" style="left:518px;top:655px">
  <div class="photo" role="img" aria-label="Hand holding a phone showing a feedback form" style="background:linear-gradient(135deg,#c9e3ef,#7fb5cc 50%,#e8d2c4)"></div>
  <h3>Mobile Forms</h3>
  <p>Lorem ipsum dolor sit amet, consectetur adipiscing elit. Donec nec dignissim lorem. Vestibulum odio ante,malesuada ac auctor vitae, mollis tempus dolor.</p>
</div>
<div class="abs card" style="left:94px;top:861px">
  <div class="photo" role="img" aria-label="Three colleagues in a meeting at a laptop" style="background:linear-gradient(135deg,#f2f2f2,#cfc6bf 55%,#8a8a8f)"></div>
  <h3>Consulting &amp; Advisory</h3>
  <p>Lorem ipsum dolor sit amet, consectetur adipiscing elit. Donec nec dignissim lorem. Vestibulum odio ante,malesuada ac auctor vitae, mollis tempus dolor.</p>
</div>
<div class="abs card" style="left:306px;top:861px">
  <div class="photo" role="img" aria-label="Man browsing floating web page panels" style="background:linear-gradient(135deg,#e6eef6,#7f9cc4 55%,#d9e4ef)"></div>
  <h3>Procurement &amp; Selection Services</h3>
  <p>Lorem ipsum dolor sit amet, consectetur adipiscing elit. Donec nec dignissim lorem. Vestibulum odio ante,malesuada ac auctor vitae, mollis tempus dolor.</p>
</div>
<div class="abs card" style="left:518px;top:861px">
  <div class="photo" role="img" aria-label="Hands typing on a mobile phone" style="background:linear-gradient(135deg,#ece6e1,#c9b2a3 55%,#eeeae6)"></div>
  <h3>Mobile SMS</h3>
  <p>Lorem ipsum dolor sit amet, consectetur adipiscing elit. Donec nec dignissim lorem. Vestibulum odio ante,malesuada ac auctor vitae, mollis tempus dolor.</p>
</div>

<footer class="abs footer">
  <h4 style="left:94px">Menu</h4>
  <ul class="menu" style="left:94px;top:31px">
    <li class="active">Home</li><li>Our team</li><li>Our values</li><li>Working with us</li><li>Our Services</li><li>Our Solutions</li><li>Get in touch</li>
  </ul>
  <h4 style="left:267px">Follow Us</h4>
  <ul class="social" style="left:267px;top:33px">
    <li><span></span>Friendhub</li><li><span></span>Chirpline</li><li><span></span>Circlepost</li><li><span></span>Pinboardly</li>
  </ul>
  <h4 style="left:446px">Contact</h4>
  <svg class="abs" style="left:446px;top:34px" width="10" height="14" viewBox="0 0 10 14"><path d="M5 1a4 4 0 0 1 4 4c0 3-4 8-4 8S1 8 1 5a4 4 0 0 1 4-4z" fill="#fff"/><circle cx="5" cy="5" r="1.5" fill="#0b8fd0"/></svg>
  <div class="abs contact" style="left:464px;top:31px">44Lorem ipsum &nbsp;Street Name<br>City Name,<br>Country Zip Code 1111111</div>
  <svg class="abs" style="left:446px;top:97px" width="8" height="11" viewBox="0 0 8 11"><path d="M3 1 1 2c-1 3 1 7 4 8l2-1-1-2-1.5.5C3 6.5 2.5 4.5 3 3.5L4.2 3z" fill="#fff"/></svg>
  <div class="abs contact" style="left:464px;top:97px">08 5550 1427</div>
  <svg class="abs" style="left:446px;top:124px" width="12" height="8" viewBox="0 0 12 8"><rect x=".5" y=".5" width="11" height="7" fill="none" stroke="#fff"/><path d="M.5.5 6 4.5 11.5.5" fill="none" stroke="#fff"/></svg>
  <div class="abs contact" style="left:464px;top:122px">sales@qoradatrix.com.au</div>
  <div class="abs map" role="img" aria-label="Street map showing the office location"></div>
</footer>
</body>
</html>
```